Business Card Design for a Handbags business

We are modernising our handbags website (see attached file for new front page) and are in need of a modern business card and a related design we can use on a small marquee at the markets, on letterhead, emails etc.

As the leather handbags we mostly import are from Italy, we want a smart modern European feel to the design. We are currently thinking about changing the name of the business from Meadowlark Handbags (see www.meadowlarkhandbags.com.au) to Vantera Handbags. Also open to other suggestions you may have that communicates the European influence and quality.

Target Market(s)

25-65 year old women (and some men)

Industry/Entity Type

Business

Contact Information for Business Card

Single or double sided - whichever creates more of an impact

Font styles to use
Serif
Sans Serif

Requirements
Must have
• Clean crisp look, slightly Italian or European look and feel to reflect where the handbags are imported from
Nice to have
• open to ideas

```html
<!DOCTYPE html>
<html lang="en">
<head>
<meta charset="utf-8">
<title>Vantera Handbags – Business Card</title>
<link rel="stylesheet" href="https://fonts.googleapis.com/css2?family=Cinzel:wght@400;600&family=Tinos&display=swap">
<style>
  :root {
    --stage: #2b2b2b;
    --card: #050505;
    --red: #e3222b;
    --white: #ffffff;
    --silver: #a9a9a9;
    --line: #d8d8d8;
  }
  * { margin: 0; padding: 0; box-sizing: border-box; }
  html, body { width: 1200px; height: 834px; overflow: hidden; }
  body {
    background: var(--stage);
    position: relative;
    font-family: "Tinos", "Times New Roman", serif;
  }
  .card {
    position: absolute;
    width: 520px;
    height: 297px;
    background: var(--card);
    box-shadow: 0 10px 30px rgba(0,0,0,.5);
    color: var(--white);
  }
  .card--front { left: 60px; top: 268px; }
  .card--back  { left: 620px; top: 268px; }

  /* front */
  .brand-ring {
    position: absolute;
    left: 210px; top: 48px;
    width: 100px; height: 100px;
  }
  .front-name {
    position: absolute;
    left: 0; right: 0; top: 170px;
    text-align: center;
    font-family: "Cinzel", serif;
    font-weight: 600;
    font-size: 29px;
    letter-spacing: 1px;
    color: var(--white);
  }
  .front-tagline {
    position: absolute;
    left: 0; right: 0; top: 210px;
    text-align: center;
    font-family: "Cinzel", serif;
    font-size: 14px;
    letter-spacing: 5px;
    color: var(--silver);
  }

  /* back */
  .back-name {
    position: absolute;
    left: 34px; top: 38px;
    font-family: "Cinzel", serif;
    font-weight: 600;
    font-size: 34px;
    letter-spacing: 1px;
    color: var(--white);
  }
  .back-tagline {
    position: absolute;
    left: 36px; top: 86px;
    font-family: "Cinzel", serif;
    font-size: 17px;
    letter-spacing: 5.5px;
    color: var(--silver);
  }
  .person {
    position: absolute;
    right: 30px; top: 130px;
    text-align: right;
  }
  .person__name {
    font-family: "Cinzel", serif;
    font-weight: 600;
    font-size: 17px;
    letter-spacing: .5px;
  }
  .person__role {
    font-family: "Cinzel", serif;
    font-size: 11px;
    letter-spacing: .5px;
    color: var(--red);
    margin-top: 1px;
  }
  .person__address {
    font-size: 11.5px;
    line-height: 15px;
    margin-top: 4px;
  }
  .divider {
    position: absolute;
    left: 34px; right: 200px; top: 186px;
    height: 1px;
    background: var(--line);
  }
  .contact-list {
    position: absolute;
    left: 34px; top: 200px;
    list-style: none;
    font-size: 12.5px;
    line-height: 19px;
  }
  .contact-list li { display: flex; align-items: center; gap: 9px; }
  .contact-list svg { width: 11px; height: 11px; fill: var(--red); flex: none; }
</style>
</head>
<body>

  <section class="card card--front" aria-label="Card front">
    <svg class="brand-ring" viewBox="0 0 100 100" aria-hidden="true">
      <circle cx="50" cy="50" r="46" fill="none" stroke="#e3222b" stroke-width="6"/>
    </svg>
    <div class="front-name">Vantera Handbags</div>
    <div class="front-tagline">Luxury Leather Handbags</div>
  </section>

  <section class="card card--back" aria-label="Card back">
    <div class="back-name">Vantera Handbags</div>
    <div class="back-tagline">Luxury Leather Handbags</div>

    <div class="person">
      <div class="person__name">Luca Moretti</div>
      <div class="person__role">Managing Director</div>
      <div class="person__address">Linden Avenue NE, Calgary<br>Alberta, T3K 1B9</div>
    </div>

    <div class="divider"></div>

    <ul class="contact-list">
      <li>
        <svg viewBox="0 0 12 12" aria-hidden="true"><path d="M3 0h6a1 1 0 0 1 1 1v10a1 1 0 0 1-1 1H3a1 1 0 0 1-1-1V1a1 1 0 0 1 1-1zm0 1.5V9.5h6V1.5z"/></svg>
        0412-555-208
      </li>
      <li>
        <svg viewBox="0 0 12 12" aria-hidden="true"><path d="M2.5 0.5l2 2.6-1.2 1.4a7 7 0 0 0 4.2 4.2l1.4-1.2 2.6 2-1.2 2A9.5 9.5 0 0 1 0.5 1.7z"/></svg>
        0733-555-419
      </li>
      <li>
        <svg viewBox="0 0 12 12" aria-hidden="true"><path d="M0 2h12v8H0zm1 1v.3l5 3.4 5-3.4V3z"/></svg>
        luca@vanterahandbags.com.au
      </li>
      <li>
        <svg viewBox="0 0 12 12" aria-hidden="true"><circle cx="6" cy="6" r="5.5" fill="none" stroke="#e3222b" stroke-width="1"/><path d="M0.5 6h11M6 0.5v11" stroke="#e3222b" stroke-width="1" fill="none"/><ellipse cx="6" cy="6" rx="2.4" ry="5.5" fill="none" stroke="#e3222b" stroke-width="1"/></svg>
        www.vanterahandbags.com.au
      </li>
    </ul>
  </section>

</body>
</html>
```